Tech business card design

We need an amazing business card design for our new business 'Brakka' a marketing tech startup based in Sydney, Australia. We provide an online marketplace for businesses to search and buy advertising media, connect with service providers and learn more about marketing. We wish to communicate 'cool tech', reliability and professionalism and design based around our logo.

Target Market(s)

Business Owners

Contact Information for Business Card

Name
Position
Email Address
Website
Phone Number

Font styles to use
Other font styles liked:
• Avenir & Avenir Next

Colors

Designer to choose colors to be used in the design.

```html
<!DOCTYPE html>
<html lang="en">
<head>
<meta charset="utf-8">
<title>Brakka Business Card</title>
<link rel="stylesheet" href="https://fonts.googleapis.com/css2?family=Mulish:wght@400;700;800;900&display=swap">
<style>
  :root {
    --backdrop: #e4e4e4;
    --card-white: #ffffff;
    --navy: #101a45;
    --navy-deep: #0d1640;
    --navy-light: #141f52;
    --navy-dark: #0b1236;
    --muted: #5a5f73;
    --pattern-light: #eef0f4;
  }
  * { box-sizing: border-box; margin: 0; padding: 0; }
  html, body {
    width: 1200px;
    height: 726px;
    overflow: hidden;
    background: var(--backdrop);
    font-family: "Mulish", "Helvetica Neue", Arial, sans-serif;
  }
  .stage {
    position: relative;
    width: 1200px;
    height: 726px;
  }
  .card {
    position: absolute;
    top: 214px;
    width: 520px;
    height: 298px;
    overflow: hidden;
    box-shadow: 0 6px 18px rgba(0, 0, 0, 0.12);
  }
  .card--front { left: 50px; background: var(--card-white); color: var(--navy); }
  .card--back { left: 630px; background: var(--navy-deep); }

  .icon-field {
    position: absolute;
    left: 0;
    top: 0;
    width: 100%;
    height: 100%;
    background: radial-gradient(ellipse 340px 200px at 0% 20%, var(--pattern-light) 0%, var(--pattern-light) 40%, rgba(255, 255, 255, 0) 100%);
  }
  .rule {
    position: absolute;
    height: 1.5px;
    background: var(--navy);
  }
  .rule--top { left: 350px; right: 0; top: 56px; }
  .rule--middle { left: 0; width: 172px; top: 170px; }
  .rule--bottom { left: 0; width: 360px; top: 264px; }

  .identity {
    position: absolute;
    left: 0;
    right: 0;
    top: 44px;
    text-align: center;
  }
  .identity__name {
    font-weight: 900;
    font-size: 19px;
    line-height: 1.2;
    letter-spacing: 0.5px;
  }
  .identity__role {
    font-weight: 400;
    font-size: 12px;
    color: var(--muted);
    margin-top: 1px;
  }
  .wordmark {
    position: absolute;
    left: 0;
    right: 0;
    top: 96px;
    text-align: center;
    font-weight: 900;
    font-size: 72px;
    line-height: 1;
    letter-spacing: -1px;
    color: var(--navy);
  }
  .contact {
    position: absolute;
    left: 0;
    right: 0;
    top: 196px;
    text-align: center;
    font-size: 13px;
    line-height: 1.35;
  }
  .contact__phone { font-weight: 800; }

  .back-pattern {
    position: absolute;
    inset: 0;
    background: linear-gradient(160deg, var(--navy-light) 0%, var(--navy-deep) 60%, var(--navy-dark) 100%);
  }
  .back-wordmark {
    position: absolute;
    right: 34px;
    bottom: 96px;
    font-weight: 900;
    font-size: 34px;
    letter-spacing: -0.5px;
    color: var(--card-white);
  }
</style>
</head>
<body>
  <main class="stage">
    <section class="card card--front" aria-label="Card front">
      <div class="icon-field" role="img" aria-label="Faint pattern of line icons for marketing and media"></div>
      <div class="rule rule--top"></div>
      <div class="rule rule--middle"></div>
      <div class="rule rule--bottom"></div>
      <div class="identity">
        <p class="identity__name">MARCUS REYL</p>
        <p class="identity__role">Managing Director</p>
      </div>
      <p class="wordmark">brakka</p>
      <div class="contact">
        <p class="contact__phone">555-204-8816</p>
        <p>info@brakkamail.com</p>
        <p>www.brakka.com</p>
      </div>
    </section>

    <section class="card card--back" aria-label="Card back">
      <div class="back-pattern" role="img" aria-label="Tonal navy pattern of repeated brand name"></div>
      <p class="back-wordmark">brakka</p>
    </section>
  </main>
</body>
</html>
```